Bref créative
Velmoran Group
Business Cards and Letterhead
Professional
Peter L. Dunmore
Founder
2700 Fenwick Lane
Suite 500
Massapequa Park, NY 11594
TBD
pete@velmoran-example.com
www.velmoran-example.com
We need to incorporate a tagline under the logo stating," Real Estate Development and Diversified Investments".
Here is where I would like to see some creativity! This is a growing, dynamic new company, so, bring your ideas.
Please try some designs with this alternate logo with black background.

```html
<!DOCTYPE html>
<html lang="en">
<head>
<meta charset="utf-8">
<title>Velmoran Group – Stationery</title>
<link href="https://fonts.googleapis.com/css2?family=Open+Sans:wght@400;600;700&display=swap" rel="stylesheet">
<style>
:root{
  --board:#1c1c1e;
  --board-2:#2a2a2d;
  --paper:#ffffff;
  --navy:#14285a;
  --blue:#2f6fb0;
  --sky:#8fb6dc;
  --ink:#3a3f4a;
  --muted:#8a8f99;
  --rule:#c9ced6;
  --grid:#b9bec6;
  --shade:#e6e8ec;
  --ghost:#eef1f5;
}
*{box-sizing:border-box;margin:0;padding:0}
html,body{width:1200px;height:672px;overflow:hidden}
body{
  position:relative;
  background:linear-gradient(135deg,var(--board-2),var(--board));
  font-family:"Open Sans",Arial,sans-serif;color:var(--ink);
}
.sheet{position:absolute;background:var(--paper);overflow:hidden}
.band{position:absolute;left:0;right:0;top:0;height:9px;background:linear-gradient(90deg,var(--navy),var(--blue) 60%,var(--sky))}
.brand{display:flex;align-items:center;gap:5px;color:var(--navy);font-weight:600;white-space:nowrap}
.brand .dot{border-radius:50%;background:var(--blue);flex:none}
.tagline{font-size:4px;color:var(--muted);white-space:nowrap}
.ghost-name{position:absolute;color:var(--ghost);font-weight:600;white-space:nowrap}

/* business cards */
.card-front{left:48px;top:41px;width:139px;height:72px}
.card-front .band{height:5px}
.card-front .who{position:absolute;right:7px;top:9px;text-align:right;line-height:1.3}
.card-front .who b{display:block;font-size:5.5px;color:var(--navy);font-weight:700}
.card-front .who span{font-size:4px;color:var(--muted)}
.card-front .brand{position:absolute;left:7px;top:30px;flex-direction:column;align-items:flex-start;gap:2px;font-size:5.5px}
.card-front .brand .dot{width:10px;height:10px}
.card-front .contact{position:absolute;right:7px;bottom:6px;text-align:right;font-size:3.6px;line-height:1.45;color:var(--muted)}
.card-back{left:192px;top:41px;width:139px;height:72px;background:#0b0b0d}
.card-back .brand{position:absolute;left:0;right:0;top:30px;justify-content:center;color:var(--paper);font-size:8px}
.card-back .brand .dot{width:11px;height:11px}
.card-back .edge{position:absolute;left:0;top:0;bottom:0;width:5px;background:linear-gradient(var(--navy),var(--blue))}

/* envelopes */
.env-back{left:48px;top:144px;width:379px;height:168px}
.env-back svg{position:absolute;inset:0}
.env-back .brand{position:absolute;left:0;right:0;top:48px;flex-direction:column;gap:3px;font-size:8px}
.env-back .brand .dot{width:16px;height:16px}
.env-front{left:48px;top:324px;width:379px;height:156px}
.env-front .band{height:6px}
.env-front .brand{position:absolute;left:14px;top:22px;font-size:8px}
.env-front .brand .dot{width:16px;height:16px}
.env-front .tag{position:absolute;left:14px;top:44px}
.env-front .return{position:absolute;left:14px;top:64px;font-size:4.5px;color:var(--muted);white-space:nowrap}
.env-front .ghost-name{right:12px;top:76px;font-size:40px}

/* letterhead */
.letterhead{left:461px;top:41px;width:302px;height:439px}
.letterhead .brand{position:absolute;left:16px;top:28px;font-size:8px}
.letterhead .brand .dot{width:18px;height:18px}
.letterhead .tag{position:absolute;left:16px;top:50px}
.letterhead .ghost-name{left:36px;top:200px;font-size:50px}
.foot{position:absolute;left:16px;right:16px;bottom:14px;border-top:1px solid var(--rule);padding-top:4px;font-size:4.5px;color:var(--muted);display:flex;justify-content:space-between;white-space:nowrap}

/* fax */
.fax{left:799px;top:41px;width:305px;height:439px}
.fax .brand{position:absolute;right:16px;top:28px;font-size:8px}
.fax .brand .dot{width:18px;height:18px}
.fax h2{position:absolute;left:16px;top:52px;font-size:11px;font-weight:700;color:var(--ink)}
.fax-table{position:absolute;left:16px;top:70px;width:273px;border-collapse:collapse;font-size:5px;color:var(--ink);white-space:nowrap}
.fax-table td{border:1px solid var(--grid);height:13px;padding:0 3px}
.fax-table .label{width:56px;background:var(--shade)}
.fax-table .checks td{border:none;height:14px;background:var(--shade)}
.box{display:inline-block;width:5px;height:5px;border:1px solid var(--ink);margin-right:3px;vertical-align:-1px}
.fax .ghost-name{left:38px;top:200px;font-size:50px}

/* email signature */
.signature{left:451px;top:504px;width:322px;height:125px}
.signature .brand{position:absolute;left:18px;top:44px;font-size:9px}
.signature .brand .dot{width:20px;height:20px}
.signature .divider{position:absolute;left:116px;top:18px;bottom:18px;width:1px;background:var(--rule)}
.signature .who{position:absolute;left:128px;top:26px}
.signature .who b{display:block;font-size:12px;color:var(--navy);font-weight:600;white-space:nowrap}
.signature .who span{font-size:6.5px;color:var(--muted)}
.signature .contact{position:absolute;left:214px;top:48px;font-size:4.8px;color:var(--muted);line-height:1.7;white-space:nowrap}
.signature .contact svg{width:5px;height:5px;vertical-align:-1px;margin-right:3px;fill:var(--blue)}
</style>
</head>
<body>

<section class="sheet card-front">
  <div class="band"></div>
  <div class="who"><b>Peter L. Dunmore</b><span>Founder</span></div>
  <div class="brand"><span class="dot"></span>Velmoran Group</div>
  <div class="contact">2700 Fenwick Lane, Suite 500<br>Massapequa Park, NY 11594<br>(516) 555-0142<br>pete@velmoran-example.com</div>
</section>

<section class="sheet card-back">
  <div class="edge"></div>
  <div class="brand"><span class="dot"></span>Velmoran Group</div>
</section>

<section class="sheet env-back">
  <svg viewBox="0 0 379 168" preserveAspectRatio="none"><polyline points="0,0 189.5,86 379,0" fill="none" stroke="#c9ced6" stroke-width="1"/></svg>
  <div class="brand"><span class="dot"></span>Velmoran Group</div>
</section>

<section class="sheet env-front">
  <div class="band"></div>
  <div class="ghost-name">Velmoran</div>
  <div class="brand"><span class="dot"></span>Velmoran Group</div>
  <div class="tag tagline">Real Estate Development and Diversified Investments</div>
  <div class="return">2700 Fenwick Lane, Suite 500, Massapequa Park, NY 11594</div>
</section>

<section class="sheet letterhead">
  <div class="band"></div>
  <div class="ghost-name">Velmoran</div>
  <div class="brand"><span class="dot"></span>Velmoran Group</div>
  <div class="tag tagline">Real Estate Development and Diversified Investments</div>
  <div class="foot"><span>2700 Fenwick Lane, Suite 500, Massapequa Park, NY 11594</span><span>pete@velmoran-example.com</span><span>www.velmoran-example.com</span></div>
</section>

<section class="sheet fax">
  <div class="band"></div>
  <div class="ghost-name">Velmoran</div>
  <div class="brand"><span class="dot"></span>Velmoran Group</div>
  <h2>FAX</h2>
  <table class="fax-table">
    <tr><td class="label">To</td><td></td><td class="label">From</td><td></td></tr>
    <tr><td class="label">Fax</td><td></td><td class="label">Phone</td><td></td></tr>
    <tr><td class="label">Number of Pages</td><td></td><td class="label">Date</td><td></td></tr>
    <tr><td class="label">Re</td><td colspan="3"></td></tr>
    <tr class="checks"><td><span class="box"></span>Urgent</td><td><span class="box"></span>For Review</td><td><span class="box"></span>Please Comment</td><td><span class="box"></span>Please Reply</td></tr>
  </table>
  <div class="foot"><span>2700 Fenwick Lane, Suite 500, Massapequa Park, NY 11594</span><span>pete@velmoran-example.com</span><span>www.velmoran-example.com</span></div>
</section>

<section class="sheet signature">
  <div class="brand"><span class="dot"></span>Velmoran Group</div>
  <div class="divider"></div>
  <div class="who"><b>Peter L. Dunmore</b><span>Founder</span></div>
  <div class="contact">
    <div><svg viewBox="0 0 10 10"><path d="M5 0a3.5 3.5 0 0 0-3.5 3.5C1.5 6 5 10 5 10s3.5-4 3.5-6.5A3.5 3.5 0 0 0 5 0z"/></svg>2700 Fenwick Lane, Suite 500</div>
    <div><svg viewBox="0 0 10 10"><path d="M2 0l2 2.5-1 1.5c1 1.5 1.5 2 3 3l1.5-1L10 8l-1.5 2C4 9.5.5 6 0 1.5z"/></svg>(516) 555-0142</div>
    <div><svg viewBox="0 0 10 10"><rect x="0" y="2" width="10" height="6"/></svg>pete@velmoran-example.com</div>
    <div><svg viewBox="0 0 10 10"><circle cx="5" cy="5" r="5"/></svg>www.velmoran-example.com</div>
  </div>
</section>

</body>
</html>
```